KRT-VB 2018 Recycling Rate Report

We need a design for our 2018 Recycling Rate Report on Expanded Polystyrene. We want to move from a larger booklet style to a two page document. The report from last year - which was done as a booklet - is attached to provide an example of our style and design.The primary items that must be included (but not limited to) the information on pages 3, 5 & 7. The graphs must include room for 2018 data.To view our typical company design/style please see our website at www.kortavale.org. Our primary RGB colors are: (187,140,9); (94,47,29); (94,138,164); and (164,167,15). Secondary RGB colors are (249,162,28) and (218,210,208). Our title/header font is DIN Next LT Pro and our copy font is Calibri 10.5 pt. We can deviate from the font specification if beneficial and welcome interesting text treatments and typography.

Target Market(s)

Recycling facilities & general public.

Font styles to use
Sans Serif

Requirements
Must have
• Information presentation must be clean and easy to reference.

```html
<!DOCTYPE html>
<html lang="en">
<head>
<meta charset="utf-8">
<title>KRT-VB 2018 EPS Recycling Rate Report</title>
<link href="https://fonts.googleapis.com/css2?family=Raleway:wght@400;500;600;700&display=swap" rel="stylesheet">
<style>
:root{
  --gold:#bb8c09;
  --brown:#5e2f1d;
  --blue:#5e8aa4;
  --olive:#a4a70f;
  --orange:#f9a21c;
  --stone:#dad2d0;
  --white:#ffffff;
  --ink:#3b3b3b;
}
*{box-sizing:border-box;margin:0;padding:0}
html,body{width:1200px;height:424px;overflow:hidden;background:var(--brown)}
body{font-family:'Raleway',sans-serif;color:var(--ink);position:relative;font-variant-numeric:lining-nums;font-feature-settings:"lnum" 1}
svg text{font-variant-numeric:lining-nums;font-feature-settings:"lnum" 1}
.panel{position:absolute;border-radius:9px}
.connector{position:absolute;background:var(--stone)}
.heading{font-weight:500;font-size:12.5px;line-height:15px;color:var(--white);letter-spacing:.2px}
.copy{font-size:6.5px;line-height:8.55px;text-align:justify;color:var(--white)}
.copy p+p{margin-top:8.5px}

/* cover card */
.cover{left:14px;top:110px;width:121px;height:202px;background:var(--white)}
.brand{position:absolute;left:15px;top:18px;display:flex;align-items:center;gap:6px}
.brand-dot{width:34px;height:34px;border-radius:50%;background:var(--gold)}
.brand-name{font-weight:700;font-size:13px;color:var(--gold)}
.cover-year{position:absolute;left:11px;top:82px;font-weight:700;font-size:41px;line-height:44px;color:var(--gold)}
.cover-title{position:absolute;right:10px;top:126px;text-align:right;font-weight:500;font-size:14px;line-height:19px;color:var(--brown)}

/* methodology */
.method{left:145px;top:20px;width:202px;height:171px;background:var(--blue);padding:10px 13px 0 13px}
.method .heading{margin-bottom:7px}

/* line chart card */
.trend{left:358px;top:20px;width:465px;height:171px;background:var(--white)}
.trend-chart{position:absolute;left:0;top:0}
.trend-note{position:absolute;left:340px;top:12px;width:112px;height:146px;background:var(--olive);border-radius:8px;padding:8px 9px;font-size:7.1px;line-height:9.35px;color:var(--white);text-align:justify}

.accent-bar{left:832px;top:20px;width:50px;height:171px;background:var(--gold)}

/* total card */
.total{left:892px;top:20px;width:294px;height:171px;background:var(--orange);overflow:hidden}
.total-photo{position:absolute;left:14px;top:16px;width:150px;height:82px;background:linear-gradient(135deg,#f4f4f2,#d9d8d6)}
.total-label{position:absolute;left:172px;top:15px;color:var(--brown)}
.total-label .big{font-size:14px;font-weight:500;line-height:15px}
.total-label .small{font-size:6.5px;line-height:8px}
.total-value{position:absolute;right:14px;top:52px;font-weight:700;font-size:53px;line-height:54px;color:var(--brown)}
.total-copy{position:absolute;left:14px;top:111px;width:266px;font-size:6.1px;line-height:8.55px;color:var(--brown);text-align:justify}

/* collection */
.collect{left:155px;top:232px;width:222px;height:172px;background:var(--olive);padding:9px 14px 0 14px}
.collect .heading{margin-bottom:9px}

/* split numbers */
.split{left:388px;top:232px;width:263px;height:172px;background:var(--white);overflow:hidden}
.photo{position:absolute;top:11px;width:108px;height:81px}
.photo-a{left:15px;background:linear-gradient(160deg,#5a5654,#c9c9c7 55%,#8d8a87)}
.photo-b{left:136px;background:linear-gradient(160deg,#7b7570,#e3e3e0 50%,#9fb3c4)}
.stat{position:absolute;top:95px}
.stat-a{left:15px}
.stat-b{left:136px}
.stat-name{font-size:14px;line-height:16px;color:#4a4a4a}
.stat-unit{font-size:6px;line-height:7px;color:#4a4a4a}
.stat-value{font-weight:700;font-size:47px;line-height:46px;margin-top:1px;letter-spacing:-.5px}
.stat-a .stat-value{color:var(--orange)}
.stat-b .stat-value{color:var(--olive)}

/* bar chart card */
.bars{left:661px;top:232px;width:525px;height:172px;background:var(--white)}
.bars-chart{position:absolute;left:0;top:0}
.bars-note{position:absolute;left:372px;top:15px;width:142px;height:145px;background:var(--blue);border-radius:8px;padding:6px 7px;font-size:7.2px;line-height:9.35px;color:var(--white);text-align:justify}
</style>
</head>
<body>

<div class="connector" style="left:135px;top:211px;width:905px;height:1px"></div>
<div class="connector" style="left:246px;top:191px;width:1px;height:21px"></div>
<div class="connector" style="left:589px;top:191px;width:1px;height:21px"></div>
<div class="connector" style="left:1040px;top:191px;width:1px;height:21px"></div>
<div class="connector" style="left:266px;top:211px;width:1px;height:21px"></div>
<div class="connector" style="left:519px;top:211px;width:1px;height:21px"></div>
<div class="connector" style="left:923px;top:211px;width:1px;height:21px"></div>

<section class="panel cover">
  <div class="brand"><span class="brand-dot"></span><span class="brand-name">KRT-VB</span></div>
  <div class="cover-year">2018</div>
  <h1 class="cover-title">EPS<br>RECYCLING<br>RATE REPORT</h1>
</section>

<section class="panel method">
  <h2 class="heading">METHODOLOGY</h2>
  <div class="copy">
    <p>The 2017 Expanded Polystyrene Recycling Rate Study was conducted by the KRT-VB to gather data to reflect both post-consumer and post-industrial recycling activity. The 2017 results are based on data received from 55 EPS manufacturers and independent recyclers in the U.S.</p>
    <p>Participation in the EPS recycling survey is voluntary and the reported data is based on the responses received. Many companies have limited resources to put towards participation in the survey, and some companies may choose not to respond due to their confidentiality policies. Therefore, because there is not 100 percent participation, the presented totals represent the minimum amount of EPS recovered for recycling.</p>
  </div>
</section>

<section class="panel trend">
  <svg class="trend-chart" width="465" height="171" viewBox="0 0 652 240" aria-label="Line chart of post-consumer EPS recycling 1990 to 2018">
    <text x="17" y="29" font-family="Raleway,sans-serif" font-size="17.5" fill="#3b3b3b">Post-Consumer EPS Recycling 1990-2018</text>
    <g stroke="#e2e2e2" stroke-width="1">
      <line x1="62" y1="50" x2="62" y2="211"/><line x1="89.7" y1="50" x2="89.7" y2="211"/><line x1="117.4" y1="50" x2="117.4" y2="211"/><line x1="145.1" y1="50" x2="145.1" y2="211"/><line x1="172.8" y1="50" x2="172.8" y2="211"/><line x1="200.5" y1="50" x2="200.5" y2="211"/><line x1="228.2" y1="50" x2="228.2" y2="211"/><line x1="255.9" y1="50" x2="255.9" y2="211"/><line x1="283.6" y1="50" x2="283.6" y2="211"/><line x1="311.3" y1="50" x2="311.3" y2="211"/><line x1="339" y1="50" x2="339" y2="211"/><line x1="366.7" y1="50" x2="366.7" y2="211"/><line x1="394.4" y1="50" x2="394.4" y2="211"/><line x1="422.1" y1="50" x2="422.1" y2="211"/><line x1="449.8" y1="50" x2="449.8" y2="211"/>
    </g>
    <line x1="48" y1="50" x2="48" y2="211" stroke="#bdbdbd"/>
    <line x1="48" y1="211" x2="455" y2="211" stroke="#bdbdbd"/>
    <g font-family="Raleway,sans-serif" font-size="6.5" fill="#555" text-anchor="end">
      <text x="40" y="213">0</text><text x="40" y="190">10</text><text x="40" y="167">20</text><text x="40" y="144">30</text><text x="40" y="121">40</text><text x="40" y="98">50</text><text x="40" y="75">60</text><text x="40" y="52">70</text>
    </g>
    <text transform="translate(23 130) rotate(-90)" font-family="Raleway,sans-serif" font-size="5.5" fill="#777" text-anchor="middle">Millions of Pounds Recycled</text>
    <g font-family="Raleway,sans-serif" font-size="6.5" fill="#555" text-anchor="middle">
      <text x="62" y="220">1990</text><text x="89.7" y="220">1992</text><text x="117.4" y="220">1994</text><text x="145.1" y="220">1996</text><text x="172.8" y="220">1998</text><text x="200.5" y="220">2000</text><text x="228.2" y="220">2002</text><text x="255.9" y="220">2004</text><text x="283.6" y="220">2006</text><text x="311.3" y="220">2008</text><text x="339" y="220">2010</text><text x="366.7" y="220">2012</text><text x="394.4" y="220">2016</text><text x="422.1" y="220">2017</text><text x="449.8" y="220">2018</text>
    </g>
    <polyline fill="none" stroke="#a4a70f" stroke-width="1.8" points="62,204.1 89.7,163.2 117.4,155.3 145.1,159.3 172.8,169.1 200.5,153.7 228.2,150.7 255.9,153.5 283.6,137.4 311.3,133.7 339,125.7 366.7,126.6 394.4,66.1 422.1,151.4"/>
    <g font-family="Raleway,sans-serif" font-size="6.5" fill="#555" text-anchor="middle">
      <text x="62" y="197">3.0</text><text x="89.7" y="156">20.8</text><text x="117.4" y="148">24.2</text><text x="145.1" y="152">22.5</text><text x="172.8" y="162">18.2</text><text x="200.5" y="146">24.9</text><text x="228.2" y="143">26.2</text><text x="255.9" y="146">25.0</text><text x="283.6" y="130">32.0</text><text x="311.3" y="126">33.6</text><text x="339" y="118">37.1</text><text x="361" y="119">36.7</text><text x="394.4" y="59">63.0</text><text x="420" y="160">25.9</text>
    </g>
  </svg>
  <div class="trend-note">The 25-year baseline shows incremental gains with more than 23 million pounds of EPS recycled annually on average. Like all commodity markets, the EPS recycling market is cyclical. The 2017 results reflect a decrease from 2016 due to the new landscape for recycling commodities and changing international markets, especially in China.</div>
</section>

<div class="panel accent-bar"></div>

<section class="panel total">
  <div class="total-photo" role="img" aria-label="Close-up photo of a white EPS foam piece stamped with a recycling code"></div>
  <div class="total-label"><div class="big">2018 Total</div><div class="small">million pounds of EPS recycled</div></div>
  <div class="total-value">65.0</div>
  <p class="total-copy">More than 65 million pounds of EPS were recycled during calendar year 2017. This figure includes 25.9 million pounds of post-consumer packaging and 39.0 million pounds of post-industrial recovery. Post-consumer is defined as any material that is recycled after its intended end-use while post-industrial recovery includes EPS facility scrap that is recycled but never served its intended purpose as a packaging material or other end-use application.</p>
</section>

<section class="panel collect">
  <h2 class="heading">COLLECTION OPTIONS<br>&amp; RESOURCES</h2>
  <div class="copy">
    <p>Not everything can be recycled all the time. In order for materials to be recycled, stable markets must exist and there must be a demand for the end products. Each community has its own guidelines for which plastics are accepted, and these can vary widely. Some locations also offer consumer drop-off access. To find out if EPS recycling is available in your area, visit www.kortavale.org</p>
    <p>For consumers that do not have access to a local drop-off center, the KRT-VB sponsors a National Mail-Back Program intended for smaller quantities of EPS which can be mailed via Postway or ParcelLine to more than 20 locations nationwide. Full instructions and a list of Mail-Back locations are available on the KRT-VB website.</p>
  </div>
</section>

<section class="panel split">
  <div class="photo photo-a" role="img" aria-label="Photo of stacked white EPS foam scrap at a recycling facility"></div>
  <div class="photo photo-b" role="img" aria-label="Photo of a worker handling a large sheet of EPS foam"></div>
  <div class="stat stat-a"><div class="stat-name">Post-Industrial</div><div class="stat-unit">(millions of pounds)</div><div class="stat-value">39.0</div></div>
  <div class="stat stat-b"><div class="stat-name">Post-Consumer</div><div class="stat-unit">(millions of pounds)</div><div class="stat-value">25.0</div></div>
</section>

<section class="panel bars">
  <svg class="bars-chart" width="525" height="172" viewBox="0 0 737 242" aria-label="Bar chart of post-consumer and post-industrial EPS recycling">
    <text x="16" y="30" font-family="Raleway,sans-serif" font-size="17" fill="#3b3b3b">EPS Recycling Post-Consumer &amp; Post-Industrial</text>
    <text x="18" y="42" font-family="Raleway,sans-serif" font-size="5.5" fill="#555">(millions of pounds)</text>
    <rect x="18" y="61" width="8" height="8" fill="#a4a70f"/>
    <text x="33" y="68" font-family="Raleway,sans-serif" font-size="6" fill="#444">POST-CONSUMER</text>
    <rect x="18" y="78" width="8" height="8" fill="#f9a21c"/>
    <text x="33" y="85" font-family="Raleway,sans-serif" font-size="6" fill="#444">POST-INDUSTRIAL</text>
    <line x1="14" y1="220" x2="510" y2="220" stroke="#cfcfcf"/>
    <g>
      <rect x="21" y="155.6" width="25" height="64.4" fill="#a4a70f"/><rect x="48" y="179.6" width="25" height="40.4" fill="#f9a21c"/>
      <rect x="91" y="155.3" width="25" height="64.7" fill="#a4a70f"/><rect x="118" y="134.9" width="25" height="85.1" fill="#f9a21c"/>
      <rect x="160" y="133.1" width="25" height="86.9" fill="#a4a70f"/><rect x="187" y="127.4" width="25" height="92.6" fill="#f9a21c"/>
      <rect x="230" y="125.1" width="25" height="94.9" fill="#a4a70f"/><rect x="257" y="72.8" width="25" height="147.2" fill="#f9a21c"/>
      <rect x="300" y="57" width="25" height="163" fill="#a4a70f"/><rect x="327" y="75.9" width="25" height="144.1" fill="#f9a21c"/>
      <rect x="370" y="153" width="25" height="67" fill="#a4a70f"/><rect x="397" y="119.1" width="25" height="100.9" fill="#f9a21c"/>
      <rect x="440" y="153" width="25" height="67" fill="#a4a70f"/><rect x="467" y="119.1" width="25" height="100.9" fill="#f9a21c"/>
    </g>
    <g font-family="Raleway,sans-serif" font-size="6" text-anchor="middle">
      <g fill="#a4a70f">
        <text x="33.5" y="152">24.9</text><text x="103.5" y="152">25.0</text><text x="172.5" y="130">33.6</text><text x="242.5" y="122">36.7</text><text x="312.5" y="53">63.0</text><text x="382.5" y="150">25.9</text><text x="452.5" y="150">25.9</text>
      </g>
      <g fill="#f9a21c">
        <text x="60.5" y="176">15.6</text><text x="130.5" y="131">32.9</text><text x="199.5" y="124">35.8</text><text x="269.5" y="69">56.9</text><text x="339.5" y="72">55.7</text><text x="409.5" y="116">39.0</text><text x="479.5" y="116">39.0</text>
      </g>
      <g fill="#444">
        <text x="46.5" y="230">2000</text><text x="116.5" y="230">2004</text><text x="185.5" y="230">2008</text><text x="255.5" y="230">2012</text><text x="325.5" y="230">2016</text><text x="395.5" y="230">2017</text><text x="465.5" y="230">2018</text>
      </g>
    </g>
  </svg>
  <div class="bars-note">Despite lower collection amounts reflected in 2017, EPS has historically enjoyed consistent growth since its inception in the early 1990's. This decrease is a direct result of export restrictions on recycled plastics and a reprocessing plant closure that previously recycled large quantities of EPS. Newer EPS recycling technologies to facilitate EPS collection and reprocessing launched in 2018 indicate growth rates will continue on an upward trend in the future.</div>
</section>

</body>
</html>
```